Tallant Family Adoption Fundraiser

The sole purpose of this card is to tell people about the fundraiser and direct them to the website that will allow them to participate.  No other contact information is needed.
Since our approach is through personal networking, this card is our sole marketing piece and needs to be effective.  We will use an image of the card for the email & Facebook outreaches we will do.  We have a very limited budget (thus the fundraiser).
We will need a quantity of 2,000 cards.  We dont need to pay for high gloss or metalic finishes, but we were thinking we probably would want a folded business card to give us more real estate to work with.
About the fundraiser (will help you understand the content needed):  Our family is adopting a young girl from Colombia, South America.  We need to raise about $15,000 to bring her home.  This fundraiser is something called a "Duck Race".  People will go to our website and 'purchase' ducks for the race.  For each duck, there will be a rubber duck in the 'race' with their own unique number on it.  On the day of the race, all of the ducks are dumped into a river.  The first ones to cross the finish line down stream is the winner.  The more ducks people put in the race in their name, the more chances they have to win the cash prizes.  We will video the race, and show it on our website.  The idea was to make this an effective and low maintenance fundraiser - nobody has to attend an event - people dont even need to know us, they only need to want to have a chance at the cash prize.  With that being said, here are some ideas of content:
- title:  "The Splendid Paddle Dash"
- "Win 1 of 3 cash prizes totalling $1,000
- www.Welcoming Little Sparrow Back.example
- The Tallant family is adopting a young girl from Colombia, South America, and needs your help to bring her home.
-  We could include a picture of her.
-  We have an icon of a Duck holding a Colombian flag - this is an icon our son created and must be used as the focal point.  We want our existing kids (3 boys) to be part of this and our son Corwin love computer animation and drawing - he created the icon.
-  People can sponsor a duck in the race or simply make their own, individual donation through the website.
-  We are using duck puns like crazy - we will even have a duck pun contest and the winners get free additional ducks in the race.
-  We want our network to be able to use these cards to get others to participate because of the cause - even if they do not know us.  That is why we thought the folded cards would be good because we would have space to put our testimony.  If cost-prohibitive, then we will settle for a 2-sided card.
We are open to suggestions, but time is absolutely of the essence.  We just got approved by Colombia, but we only have 2 weeks left to network with folks in our schools before they are done for the year.  We need a very quick turn-around.

Updates
Due to a browser issue, the icon was not uploaded in my brief.  They are in the process of manually adding it to my brief now and should be available shortly. Thank you for your help.

Target Market(s)
Potential donors/sponsors
Industry/Entity Type
Real Estate
Contact Information for Business Card
www.WelcomingLittleSparrowBack.example
Requirements
Must have
- Catchy but simple exterior to make people want to see the interior of a folded business card.

```html
<!DOCTYPE html>
<html lang="en">
<head>
<meta charset="utf-8">
<title>The Splendid Paddle Dash – Folded Card</title>
<link rel="stylesheet" href="https://fonts.googleapis.com/css2?family=Bebas+Neue&family=Arimo:wght@500;700&display=swap">
<style>
  :root {
    --royal-blue: #263a8c;
    --navy-ink: #22357e;
    --sun-yellow: #f5e61c;
    --brick-red: #c1362a;
    --paper-white: #ffffff;
    --backdrop: #ffffff;
    --display: "Bebas Neue", "Oswald", sans-serif;
    --body: "Arimo", Arial, sans-serif;
  }
  * { box-sizing: border-box; margin: 0; padding: 0; }
  html, body { width: 1200px; height: 1200px; overflow: hidden; background: var(--backdrop); }
  .canvas { position: relative; width: 1200px; height: 1200px; }

  .panel { position: absolute; left: 271px; width: 657px; height: 560px; overflow: hidden; }
  .panel--outside { top: 30px; background: var(--royal-blue); }
  .panel--inside { top: 610px; background: var(--brick-red); }

  /* Outside panel */
  .intro-oval {
    position: absolute; left: 17px; top: 26px; width: 312px; height: 220px;
    border-radius: 50%; background: var(--paper-white);
    display: flex; align-items: center; justify-content: center; text-align: center;
    font-family: var(--display); color: var(--navy-ink); font-size: 23px; line-height: 1.2; letter-spacing: 0.3px;
    padding: 0 24px;
  }
  .site-invite {
    position: absolute; left: 0; top: 290px; width: 330px; text-align: center;
    font-family: var(--display); color: var(--paper-white); font-size: 20px; line-height: 1.42;
  }
  .site-invite .site-url { color: var(--sun-yellow); font-size: 19px; white-space: nowrap; }
  .duck-icon { position: absolute; border-radius: 40% 40% 45% 45%; }
  .duck-icon--small {
    left: 80px; top: 384px; width: 142px; height: 136px;
    background: linear-gradient(180deg, var(--sun-yellow) 0%, var(--sun-yellow) 45%, #c63a32 75%, #2a3f95 100%);
  }
  .duck-icon--large {
    left: 344px; top: 178px; width: 291px; height: 282px;
    background: linear-gradient(180deg, var(--sun-yellow) 0%, var(--sun-yellow) 50%, #2a3f95 72%, #c63a32 100%);
  }
  .event-title { position: absolute; left: 348px; top: 28px; width: 290px; text-align: center; font-family: var(--display); font-weight: 400; }
  .event-title__lead { display: block; color: var(--paper-white); font-size: 52px; line-height: 1; }
  .event-title__main { display: block; color: var(--sun-yellow); font-size: 66px; line-height: 1; }
  .prize-line {
    position: absolute; left: 352px; top: 470px; width: 290px; text-align: center; font-family: var(--body); font-weight: 500;
  }
  .prize-line__count { display: block; color: var(--paper-white); font-size: 20px; }
  .prize-line__total { display: block; color: var(--sun-yellow); font-size: 25px; margin-top: 4px; }

  /* Inside panel */
  .photo-frame {
    position: absolute; left: 21px; top: 59px; width: 287px; height: 375px; background: var(--paper-white);
    display: flex; align-items: center; justify-content: center; text-align: center;
    font-family: var(--display); color: var(--brick-red); font-size: 46px; line-height: 1.2;
  }
  .inside-url {
    position: absolute; left: 14px; top: 450px; width: 301px; text-align: center; white-space: nowrap;
    font-family: var(--display); color: var(--paper-white); font-size: 19px;
  }
  .testimonial { position: absolute; width: 300px; height: 100px; margin: 0; }
  .testimonial svg { position: absolute; inset: 0; width: 100%; height: 100%; }
  .testimonial__quote {
    position: absolute; left: 0; top: 0; width: 100%; height: 83px; margin: 0;
    display: flex; align-items: center; justify-content: center; text-align: center;
    font-family: var(--display); color: var(--brick-red); font-size: 19px; line-height: 1.15; padding: 0 24px;
  }
  .testimonial--one { left: 342px; top: 35px; }
  .testimonial--two { left: 342px; top: 234px; }
  .testimonial--three { left: 342px; top: 412px; }
  .testimonial-name { position: absolute; font-family: var(--display); color: var(--paper-white); font-size: 20px; line-height: 1; }
  .testimonial-name--one { left: 352px; top: 150px; }
  .testimonial-name--two { left: 540px; top: 340px; }
  .testimonial-name--three { left: 352px; top: 522px; }
</style>
</head>
<body>
<main class="canvas">
  <section class="panel panel--outside" aria-label="Card outside">
    <p class="intro-oval">The Tallant family is<br>adopting a young girl from<br>Colombia, South America,<br>and needs your help<br>to bring her home</p>
    <p class="site-invite">Please visit our site<br><span class="site-url">www.WelcomingLittleSparrowBack.example</span><br>And join the charity duck race!</p>
    <div class="duck-icon duck-icon--small" role="img" aria-label="Small version of the duck icon holding a Colombian flag"></div>
    <h1 class="event-title"><span class="event-title__lead">The Splendid</span><span class="event-title__main">Paddle Dash</span></h1>
    <div class="duck-icon duck-icon--large" role="img" aria-label="Duck icon in sunglasses waving a Colombian flag, with smaller flag-waving ducks behind"></div>
    <p class="prize-line"><span class="prize-line__count">WIN 1 OF 3 CASH PRIZES</span><span class="prize-line__total">TOTALLING $1,000!!</span></p>
  </section>

  <section class="panel panel--inside" aria-label="Card inside">
    <div class="photo-frame">Insert<br>daughter photo<br>here</div>
    <p class="inside-url">www.WelcomingLittleSparrowBack.example</p>

    <figure class="testimonial testimonial--one">
      <svg viewBox="0 0 300 100" aria-hidden="true"><ellipse cx="148" cy="41" rx="146" ry="41" fill="#fff"/><path d="M22 66 L18 94 L48 76 Z" fill="#fff"/></svg>
      <blockquote class="testimonial__quote">“This is a<br>fun event for a good cause,<br>what are you waiting for?”</blockquote>
    </figure>
    <p class="testimonial-name testimonial-name--one">John Doe</p>

    <figure class="testimonial testimonial--two">
      <svg viewBox="0 0 300 100" aria-hidden="true"><ellipse cx="150" cy="41" rx="149" ry="41" fill="#fff"/><path d="M238 74 L258 94 L262 68 Z" fill="#fff"/></svg>
      <blockquote class="testimonial__quote">“I know the Tallant family and<br>she’ll feel right at home”</blockquote>
    </figure>
    <p class="testimonial-name testimonial-name--two">Jane Doe</p>

    <figure class="testimonial testimonial--three">
      <svg viewBox="0 0 300 100" aria-hidden="true"><ellipse cx="150" cy="41" rx="149" ry="41" fill="#fff"/><path d="M26 66 L22 94 L52 76 Z" fill="#fff"/></svg>
      <blockquote class="testimonial__quote">“Good luck to the Tallant family<br>and good luck to my duck :)”</blockquote>
    </figure>
    <p class="testimonial-name testimonial-name--three">Jim Doe</p>
  </section>
</main>
</body>
</html>
```